Home Services- Spring Clean Options

Brightwell Crew provides a variety of Home Services- focused on cleaning & improving the exterior of the home:

 Power Washing- driveways, sidewalks, patios, decks, fence
 Fence Staining- make fence look new with variety of staining colors
 Gutter cleaning- important to make sure have proper Water Drainage
 Gutter Guard Installation- prevent damage to roof and house by keeping debris out of gutters and water flowing.
 Window Washing- our exterior washing team and reach the highest windows
 Landscape& Patio Lights- highlight areas for beauty and safety
Updates

We are are almost finished. Just please make sure you pay attention to the wording and grammer in Red thx

Target Market(s)

Middle to Upper level Home Owners (especially women)

Industry/Entity Type

Cleaning Services

Font styles to use
Serif
Sans Serif

Requirements
Must have
• Not be Cluttered- Clean friendly, professional look. Focus on the Professional

Info@GoBrightwellCrew.com
972-648-0000
Nice to have
• Pictures of services- these are just examples
Should not have
• Bigger and bolder Services & Specials. Want to Show all the Services we offer but do Not use too much detail- don't want it to look "cluttered"

```html
<!DOCTYPE html>
<html lang="en">
<head>
<meta charset="utf-8">
<title>Home Services – Spring Clean | Brightwell Crew</title>
<link href="https://fonts.googleapis.com/css2?family=Barlow+Condensed:wght@300;400;500;600;700&family=Open+Sans:wght@400;600&display=swap" rel="stylesheet">
<style>
  :root{
    --page-bg:#e4e4e4;
    --navy:#0f3f78;
    --blue:#1a5fa8;
    --sky:#4aa3e0;
    --sky-light:#bfe1f7;
    --yellow:#fff200;
    --white:#ffffff;
    --ink:#222222;
    --title-blue:#114a8a;
    --divider:#8a8a8a;
  }
  *{box-sizing:border-box;margin:0;padding:0}
  html,body{width:1200px;height:1000px;overflow:hidden;background:var(--page-bg)}
  ul{list-style:none}
  .flyer{position:absolute;left:285px;top:57px;width:623px;height:881px;background:var(--white);overflow:hidden}
  .flyer-art{position:absolute;left:0;top:0}
  .headline{position:absolute;left:37px;top:82px;font-family:"Barlow Condensed",sans-serif;font-weight:600;line-height:1;text-shadow:0 2px 6px rgba(0,0,0,.45)}
  .headline-top{display:block;color:var(--white);font-size:57px;letter-spacing:.5px}
  .headline-main{display:block;color:var(--yellow);font-size:76px;margin-top:2px;letter-spacing:.5px}
  .intro{position:absolute;left:40px;top:360px;font-family:"Barlow Condensed",sans-serif;text-transform:uppercase}
  .intro-name{color:var(--white);font-weight:300;font-size:27px;line-height:28px}
  .intro-lead{color:var(--yellow);font-weight:700;font-size:30px;line-height:28px;margin-top:4px}
  .intro-focus{color:var(--white);font-weight:400;font-size:18px;line-height:21px;margin-top:10px}
  .services{position:absolute;font-family:"Open Sans",sans-serif;font-size:15px;line-height:20px;color:var(--ink)}
  .service{position:absolute;left:0;width:240px}
  .service-icon{position:absolute;left:-70px;top:-4px;width:46px;height:46px}
  .service-name{color:var(--title-blue);font-weight:600}
  .services-left{left:107px;top:569px}
  .services-right{left:402px;top:606px}
  .column-divider{position:absolute;left:312px;top:518px;width:2px;height:305px;background:var(--divider)}
  .contact-bar{position:absolute;left:0;bottom:0;width:623px;height:43px;background:linear-gradient(var(--blue),var(--navy));display:flex;align-items:center;justify-content:center;gap:10px;font-family:"Open Sans",sans-serif;font-size:13.5px;color:var(--white);white-space:nowrap}
  .contact-item{display:flex;align-items:center;gap:6px}
  .contact-sep{width:2px;height:24px;background:var(--sky)}
</style>
</head>
<body>
<main class="flyer">
  <svg class="flyer-art" width="623" height="881" viewBox="0 0 623 881">
    <defs>
      <linearGradient id="photoTone" x1="0" y1="0" x2="1" y2="1">
        <stop offset="0" stop-color="#6f8a5a"/><stop offset=".5" stop-color="#4f6b3c"/><stop offset="1" stop-color="#9c7e6c"/>
      </linearGradient>
      <linearGradient id="waveDark" x1="0" y1="0" x2="0" y2="1">
        <stop offset="0" stop-color="#2468b0"/><stop offset="1" stop-color="#0d3a70"/>
      </linearGradient>
      <linearGradient id="waveLight" x1="0" y1="0" x2="1" y2="0">
        <stop offset="0" stop-color="#3b92d6"/><stop offset="1" stop-color="#8ec9ef"/>
      </linearGradient>
      <radialGradient id="iconFill" cx=".4" cy=".35" r=".7">
        <stop offset="0" stop-color="#3d8fd6"/><stop offset="1" stop-color="#0f4b8a"/>
      </radialGradient>
    </defs>
    <rect role="img" aria-label="Photo of a worker power washing a garden patio beside a house" x="0" y="0" width="623" height="340" fill="url(#photoTone)"/>
    <path d="M0,262 C140,240 250,262 330,330 L330,360 L0,360 Z" fill="url(#waveLight)"/>
    <path d="M0,276 C140,258 240,280 318,345 L318,360 L0,360 Z" fill="var(--sky-light)"/>
    <path d="M0,328 C130,300 240,318 300,355 C320,400 300,460 240,500 C190,535 120,548 60,540 C30,536 10,530 0,528 Z" fill="url(#waveDark)"/>
    <circle role="img" aria-label="Photo of a family grilling on a backyard patio" cx="518" cy="398" r="156" fill="#4d6a3e" stroke="var(--yellow)" stroke-width="5"/>
    <circle role="img" aria-label="Photo of a worker washing an exterior window" cx="372" cy="404" r="94" fill="#8fa4b6" stroke="var(--yellow)" stroke-width="5"/>
    <circle role="img" aria-label="Photo of a patio lit with string lights at night" cx="432" cy="525" r="79" fill="#3a3528" stroke="var(--yellow)" stroke-width="5"/>
  </svg>

  <h1 class="headline">
    <span class="headline-top">HOME SERVICES-</span>
    <span class="headline-main">SPRING CLEAN</span>
  </h1>

  <section class="intro">
    <p class="intro-name">Brightwell Crew</p>
    <p class="intro-lead">Provides a variety<br>of home services-</p>
    <p class="intro-focus">Focused on cleaning &amp; improving<br>the exterior of the home:</p>
  </section>

  <div class="column-divider"></div>

  <ul class="services services-left">
    <li class="service" style="top:0">
      <svg class="service-icon" viewBox="0 0 46 46"><circle cx="23" cy="23" r="23" fill="url(#iconFill)"/><rect x="17" y="12" width="10" height="16" rx="2" fill="none" stroke="#fff" stroke-width="2"/><path d="M22 28v5h8" fill="none" stroke="#fff" stroke-width="2"/></svg>
      <span class="service-name">Power Washing</span>- driveways,<br>sidewalks, patios,<br>decks, fence
    </li>
    <li class="service" style="top:74px">
      <svg class="service-icon" viewBox="0 0 46 46"><circle cx="23" cy="23" r="23" fill="url(#iconFill)"/><path d="M13 30V18h20v12M13 22h20M13 26h20" fill="none" stroke="#fff" stroke-width="2"/></svg>
      <span class="service-name">Fence Staining</span>- make fence<br>look new with variety of<br>staining colors
    </li>
    <li class="service" style="top:150px">
      <svg class="service-icon" viewBox="0 0 46 46"><circle cx="23" cy="23" r="23" fill="url(#iconFill)"/><path d="M12 20h22l-3 10H15z" fill="none" stroke="#fff" stroke-width="2"/><path d="M16 15h14" stroke="#fff" stroke-width="2"/></svg>
      <span class="service-name">Gutter Guard Installation</span>-<br>prevent damage to roof<br>and house by keeping<br>debris out of gutters and<br>water flowing.
    </li>
  </ul>

  <ul class="services services-right">
    <li class="service" style="top:0">
      <svg class="service-icon" viewBox="0 0 46 46"><circle cx="23" cy="23" r="23" fill="url(#iconFill)"/><rect x="13" y="14" width="20" height="18" fill="none" stroke="#fff" stroke-width="2"/><path d="M13 20h20M13 26h20M20 14v18M26 14v18" stroke="#fff" stroke-width="1.5"/></svg>
      <span class="service-name">Gutter cleaning</span>- important<br>to make sure have proper<br>Water Drainage
    </li>
    <li class="service" style="top:76px">
      <svg class="service-icon" viewBox="0 0 46 46"><circle cx="23" cy="23" r="23" fill="url(#iconFill)"/><rect x="13" y="13" width="20" height="20" fill="none" stroke="#fff" stroke-width="2"/><path d="M23 13v20M13 23h20" stroke="#fff" stroke-width="1.5"/></svg>
      <span class="service-name">Window Washing</span>- our<br>exterior washing team and<br>reach the highest windows
    </li>
    <li class="service" style="top:153px">
      <svg class="service-icon" viewBox="0 0 46 46"><circle cx="23" cy="23" r="23" fill="url(#iconFill)"/><path d="M17 12h12l-3 9h-6z" fill="#fff"/><path d="M23 21v13M18 34h10" stroke="#fff" stroke-width="2"/></svg>
      <span class="service-name">Landscape&amp; Patio Lights</span>-<br>highlight areas for beauty<br>and safety
    </li>
  </ul>

  <footer class="contact-bar">
    <span class="contact-item">
      <svg width="15" height="15" viewBox="0 0 16 16"><path d="M3 1l3 3-2 2c1 2 3 4 5 5l2-2 3 3-2 3C7 15 1 9 1 3z" fill="var(--yellow)"/></svg>
      972-648-0000
    </span>
    <span class="contact-sep"></span>
    <span class="contact-item">
      <svg width="17" height="12" viewBox="0 0 18 13"><rect width="18" height="13" fill="var(--yellow)"/><path d="M0 0l9 7 9-7" fill="none" stroke="var(--navy)" stroke-width="1.5"/></svg>
      Info@GoBrightwellCrew.com
    </span>
    <span class="contact-sep"></span>
    <span class="contact-item">
      <svg width="15" height="15" viewBox="0 0 16 16"><circle cx="8" cy="8" r="7" fill="none" stroke="var(--yellow)" stroke-width="1.5"/><ellipse cx="8" cy="8" rx="3" ry="7" fill="none" stroke="var(--yellow)" stroke-width="1.2"/><path d="M1 8h14" stroke="var(--yellow)" stroke-width="1.2"/></svg>
      www.gobrightwellcrew.com
    </span>
  </footer>
</main>
</body>
</html>
```